Bramwell Exteriors Needs a New Website!

We are an exteriors company specializing in vinyl siding, Northcrest siding, aluminum soffit/fascia, trough. We do new construction work as well as renovations. We also build detached garages.
You can view our current website at www.bramwellbuilders.ca
I want to completely overhaul the website.
Our services are different now as we no longer do new home construction as well as we do not do the snow clearing.
I want to focus on 2 things in particular on the website:

1/ Exterior renovations

2/ Detached Garage construction.

I have included our logo in the attached files to use as well.

Some features we would like:

1/ Be able to easily attach a video from Youtube/Vimeo to highlight a product or service
2/ Quick chat or contact button that we can talk to a potential client quickly
3/ Meet the Team page that is interesting and fresh
4/ Place for us to put in helpful exterior tips/suggestions for homeowners.

Content is not important, but looking for the best design that will attract people once they click on our page and want to renovate with us.

Target Market(s)

People looking for renovations on their home, people looking to build a detached garage.

Industry/Entity Type

Residential Construction

Coding

Coded - Design and coding required

Number of Pages Required

5+ page

Font styles to use
Sans Serif

Requirements
Must have
• Fresh and exciting home page.

Simple design. Don't want it over complicated or too much information to confuse the potential client.

Easy way to contact us.

Meet the team page that instills confidence
Nice to have
• Colour of website to go off our logo. Doesn't need to be an exact match, but something that goes well with our blue and grey.

```html
<!DOCTYPE html>
<html lang="en">
<head>
<meta charset="utf-8">
<title>Bramwell Exteriors</title>
<link rel="stylesheet" href="https://fonts.googleapis.com/css2?family=Barlow:wght@400;500;600&family=Barlow+Semi+Condensed:wght@400;500&display=swap">
<style>
:root{
  --blue:#0b68c6;
  --navy:#262b38;
  --footer:#3a3f4c;
  --ink:#1e2128;
  --body:#666a72;
  --field:#ffffff;
  --panel:#eef0f3;
  --white:#ffffff;
}
*{box-sizing:border-box;margin:0;padding:0}
html,body{width:1200px;height:4299px;overflow:hidden}
body{position:relative;background:var(--white);font-family:"Barlow",Arial,sans-serif;color:var(--ink)}
.abs{position:absolute}
.heading{font-family:"Barlow Semi Condensed","Barlow",sans-serif;font-weight:500}
.eyebrow{font-size:14px;letter-spacing:.6px;color:var(--blue);font-weight:500;text-transform:uppercase}
.center{left:0;width:1200px;text-align:center}
.photo{position:absolute}
.btn{position:absolute;display:flex;align-items:center;justify-content:center;border-radius:20px;font-size:13px;font-weight:500}
.btn-solid{background:var(--blue);color:var(--white)}
.btn-line{border:2px solid var(--blue);color:var(--blue)}
.circle-arrow{position:absolute;width:40px;height:40px;border-radius:50%;border:2px solid currentColor;display:flex;align-items:center;justify-content:center}

/* header */
.site-header{left:0;top:0;width:1200px;height:80px;background:var(--white)}
.brand{left:87px;top:22px;display:flex;align-items:center;gap:8px}
.brand-dot{width:34px;height:34px;border-radius:50%;background:var(--blue)}
.brand-name{font-size:22px;font-weight:600;color:var(--blue)}
.nav a{position:absolute;top:31px;font-size:13px;color:var(--ink);text-decoration:none}
.nav a.active{color:var(--blue)}
.call{left:783px;top:31px;font-size:13px;color:var(--blue);display:flex;align-items:center;gap:5px}
.call b{color:var(--ink);font-weight:500}

/* hero */
.hero{left:0;top:80px;width:1200px;height:479px;background:linear-gradient(180deg,#6d7683 0%,#59606c 45%,#6d5a4a 78%,#4f5b3b 100%)}
.hero-shade{left:0;top:80px;width:1200px;height:479px;background:rgba(20,24,32,.28)}
.hero-sub{top:226px;font-size:14px;letter-spacing:.6px;color:var(--white);font-weight:500}
.hero-title{top:258px;font-size:37px;line-height:46px;color:var(--white)}

/* services */
.svc-title{top:660px;font-size:35px;color:var(--ink)}
.card-img{height:201px}
.card-tab{width:41px;height:38px}
.card-h{font-size:19px}
.card-p{font-size:12px;line-height:19.5px;color:var(--body);width:282px}
.readmore{font-size:12px;font-weight:600;display:flex;align-items:center;gap:6px}

/* about */
.about{left:0;top:1163px;width:1200px;height:561px;background:var(--navy)}
.about-title{left:616px;top:1272px;font-size:37px;line-height:46px;color:var(--white)}
.about-p{left:616px;top:1430px;width:500px;font-size:13px;line-height:24px;color:#dfe2e8}
.years{left:88px;top:1580px;width:303px;height:64px;background:var(--blue);color:var(--white);display:flex;align-items:center;justify-content:center;gap:12px}
.years strong{font-family:"Barlow Semi Condensed",sans-serif;font-size:34px;font-weight:500}
.years span{font-size:14px;font-weight:600}

/* team */
.team-title{top:1828px;font-size:35px}
.member{width:240px}
.member-photo{height:271px}
.member-name{width:240px;height:46px;display:flex;align-items:center;justify-content:center;font-size:16px;font-weight:500;border-bottom:2px solid var(--blue)}
.member-featured{background:var(--blue);color:var(--white)}
.role{font-size:12px;color:var(--white);transform:rotate(-90deg);transform-origin:left top;white-space:nowrap;font-weight:500}

/* video + tips */
.blue-band{left:0;top:2555px;width:1200px;height:791px;background:var(--blue)}
.video{left:88px;top:2375px;width:1024px;height:359px;background:linear-gradient(180deg,#8593a6 0%,#6c7480 40%,#566648 75%,#4b5d3a 100%)}
.video-shade{left:88px;top:2375px;width:1024px;height:359px;background:rgba(20,30,45,.3)}
.video-title{top:2544px;font-size:36px;line-height:46px;color:var(--white)}
.tips-title{top:2836px;font-size:36px;color:var(--white)}
.tips{left:207px;top:2912px;width:784px;color:var(--white)}
.tip{border-top:1px solid rgba(255,255,255,.55);position:relative}
.tip:last-child{border-bottom:1px solid rgba(255,255,255,.55)}
.tip-q{height:48px;display:flex;align-items:center;justify-content:space-between;padding:0 32px;font-size:14px;font-weight:500}
.tip-a{padding:0 64px 18px 32px;font-size:12px;line-height:24px;color:#e3ecf7;margin-top:-6px}

/* quote */
.quote-title{left:207px;top:3572px;font-size:36px}
.quote-p{left:207px;top:3630px;width:345px;font-size:13px;line-height:19.5px;color:var(--body)}
.form{left:616px;top:3420px;width:375px;height:462px;background:var(--panel)}
.field{left:648px;width:312px;height:40px;background:var(--field);border-radius:20px;padding:0 22px;display:flex;align-items:center;justify-content:space-between;font-size:11px;color:#7a7f88}
.field-msg{height:108px;border-radius:16px;align-items:flex-start;padding-top:20px}

/* footer */
.footer{left:0;top:3964px;width:1200px;height:335px;background:var(--footer)}
.footer-text{color:#c9ced8;font-size:12px}
.f-h{font-size:16px;color:var(--white);font-weight:500}
.social{width:28px;height:28px;border-radius:50%;border:1.5px solid var(--blue)}
</style>
</head>
<body>

<header class="abs site-header">
  <div class="abs brand"><span class="brand-dot"></span><span class="brand-name">Bramwell Exteriors</span></div>
  <nav class="nav">
    <a class="active" style="left:405px">Home</a>
    <a style="left:471px">Services</a>
    <a style="left:554px">Meet The Team</a>
    <a style="left:674px">Contact Us</a>
  </nav>
  <div class="abs call">Call Us:
    <svg width="13" height="13" viewBox="0 0 24 24" fill="none" stroke="currentColor" stroke-width="2"><path d="M22 16.9v3a2 2 0 0 1-2.2 2 19.8 19.8 0 0 1-8.6-3.1 19.5 19.5 0 0 1-6-6A19.8 19.8 0 0 1 2.1 4.2 2 2 0 0 1 4.1 2h3a2 2 0 0 1 2 1.7c.1.9.4 1.8.7 2.7a2 2 0 0 1-.5 2.1L8 9.8a16 16 0 0 0 6 6l1.3-1.3a2 2 0 0 1 2.1-.4c.9.3 1.8.6 2.7.7a2 2 0 0 1 1.7 2z"/></svg>
    <b>780-555-0148</b></div>
  <div class="btn btn-solid" style="left:968px;top:23px;width:144px;height:32px">Request A Quote</div>
</header>

<div class="abs hero" role="img" aria-label="Photo of a renovated two-storey home with stone and siding exterior"></div>
<div class="abs hero-shade"></div>
<p class="abs center hero-sub">WE PROVIDE QUALITY SERVICES FOR</p>
<h1 class="abs center heading hero-title">Home Exterior Renovations &amp; Detached<br>Garage Construction</h1>
<div class="btn btn-solid" style="left:536px;top:380px;width:127px;height:30px">Contact Us</div>
<div class="circle-arrow" style="left:88px;top:282px;color:#fff">
  <svg width="12" height="12" viewBox="0 0 12 12" fill="none" stroke="currentColor" stroke-width="1.5"><path d="M8 1 3 6l5 5"/></svg></div>
<div class="circle-arrow" style="left:1072px;top:282px;color:#fff">
  <svg width="12" height="12" viewBox="0 0 12 12" fill="none" stroke="currentColor" stroke-width="1.5"><path d="m4 1 5 5-5 5"/></svg></div>

<p class="abs center eyebrow" style="top:636px">Our Services</p>
<h2 class="abs center heading svc-title">What We Do</h2>

<div class="photo card-img" style="left:207px;top:729px;width:377px;background:linear-gradient(180deg,#7fb2e4 0%,#b8d2ea 40%,#6f7a72 70%,#5c8a45 100%)" role="img" aria-label="Photo of a renovated house with double garage"></div>
<div class="abs card-tab" style="left:543px;top:930px;background:#8a8f98"></div>
<h3 class="abs heading card-h" style="left:232px;top:956px;color:var(--blue)">Exterior Renovations</h3>
<p class="abs card-p" style="left:232px;top:992px">It is a long established fact that a reader will be distracted by the readable content of a page when looking at its layout ...</p>
<div class="abs readmore" style="left:232px;top:1071px;color:var(--blue)">Read More
  <svg width="10" height="8" viewBox="0 0 10 8" fill="none" stroke="currentColor" stroke-width="1.3"><path d="M0 4h9M6 1l3 3-3 3"/></svg></div>

<div class="photo card-img" style="left:616px;top:729px;width:375px;background:linear-gradient(180deg,#5f9fdc 0%,#a7c8e6 40%,#c9c3b5 70%,#5e8c44 100%)" role="img" aria-label="Photo of a home with a newly built detached garage"></div>
<div class="abs card-tab" style="left:951px;top:930px;background:var(--navy)"></div>
<h3 class="abs heading card-h" style="left:640px;top:956px">Detached Garage Construction</h3>
<p class="abs card-p" style="left:640px;top:992px">It is a long established fact that a reader will be distracted by the readable content of a page when looking at its layout ...</p>
<div class="abs readmore" style="left:640px;top:1071px">Read More
  <svg width="10" height="8" viewBox="0 0 10 8" fill="none" stroke="currentColor" stroke-width="1.3"><path d="M0 4h9M6 1l3 3-3 3"/></svg></div>

<section class="abs about"></section>
<div class="photo" style="left:88px;top:1243px;width:352px;height:321px;background:linear-gradient(180deg,#b9cfe3 0%,#6a7688 45%,#4c5463 70%,#5b7a44 100%)" role="img" aria-label="Photo of a modern grey two-storey home"></div>
<div class="photo" style="left:352px;top:1435px;width:207px;height:209px;background:linear-gradient(180deg,#eef0ee 0%,#8fa27b 40%,#6fb4c9 65%,#a97b52 100%);border-top:6px solid var(--navy);border-left:6px solid var(--navy)" role="img" aria-label="Photo of a backyard patio next to a pool"></div>
<div class="abs years"><strong>30</strong><span>Years Eperience</span></div>
<p class="abs eyebrow" style="left:616px;top:1240px">Welcome to Bramwell Exteriors</p>
<h2 class="abs heading about-title">Succefull Business for<br>Exterior Renovations and<br>Construction</h2>
<p class="abs about-p">It is a long established fact that a reader will be distracted by the readable content of a page when looking at its layout. The point of using Lorem Ipsum is that it has a more-or-less normal distribution of letters, as opposed to using 'Content here, content here', making it look like readable English. Many desktop publishing packages and web page editors now use Lorem Ipsum as their default model text, and a search for 'lorem ipsum.</p>
<div class="btn btn-line" style="left:616px;top:1614px;width:143px;height:30px">Request A Quote</div>

<p class="abs center eyebrow" style="top:1803px">Our Team</p>
<h2 class="abs center heading team-title">Meet the Experts</h2>
<div class="circle-arrow" style="left:127px;top:2020px;color:var(--blue)">
  <svg width="12" height="12" viewBox="0 0 12 12" fill="none" stroke="currentColor" stroke-width="1.5"><path d="M8 1 3 6l5 5"/></svg></div>
<div class="circle-arrow" style="left:1031px;top:2020px;color:var(--blue)">
  <svg width="12" height="12" viewBox="0 0 12 12" fill="none" stroke="currentColor" stroke-width="1.5"><path d="m4 1 5 5-5 5"/></svg></div>

<div class="abs member" style="left:207px;top:1904px">
  <div class="member-photo" style="background:linear-gradient(180deg,#b9ad7c 0%,#8d8e6c 40%,#9fb3c8 75%,#8ea4bb 100%)" role="img" aria-label="Portrait photo of team member Colin Harwood"></div>
  <div class="member-name">Colin Harwood</div>
</div>
<div class="abs member member-featured" style="left:479px;top:1904px">
  <div class="member-photo" style="margin-left:32px;width:208px;background:linear-gradient(180deg,#c5b98a 0%,#9c966b 40%,#7d90a8 75%,#6f86a3 100%)" role="img" aria-label="Portrait photo of team member Owen Prescott"></div>
  <div class="member-name">Owen Prescott</div>
  <div class="abs role" style="left:9px;top:226px">Operations Manager (Exteriors)</div>
</div>
<div class="abs member" style="left:751px;top:1904px">
  <div class="member-photo" style="background:linear-gradient(180deg,#c6b987 0%,#a59a70 40%,#a3b3c4 75%,#93a5b8 100%)" role="img" aria-label="Portrait photo of team member Arlo Vandermeer"></div>
  <div class="member-name">Arlo Vandermeer</div>
</div>
<div class="btn btn-line" style="left:527px;top:2265px;width:144px;height:30px">View All Team</div>

<section class="abs blue-band"></section>
<div class="abs video" role="img" aria-label="Video cover photo of a large family home with a paved driveway"></div>
<div class="abs video-shade"></div>
<svg class="abs" style="left:578px;top:2489px" width="42" height="42" viewBox="0 0 42 42" fill="none" stroke="#fff" stroke-width="2.5"><circle cx="21" cy="21" r="19"/><path d="M17 13v16l12-8z"/></svg>
<h2 class="abs center heading video-title">Dream Home Might Be Closer<br>Than You are Thinking</h2>

<p class="abs center eyebrow" style="top:2813px;color:#fff">Suggestions</p>
<h2 class="abs center heading tips-title">Helpful Exterior Tips</h2>
<div class="abs tips">
  <div class="tip"><div class="tip-q">Refresh the exterior of your home<span>+</span></div></div>
  <div class="tip"><div class="tip-q">Outdoor dining and entertaining areas<span>−</span></div>
    <p class="tip-a">It is a long established fact that a reader will be distracted by the readable content of a page when looking at its layout. The point of using Lorem Ipsum is that it has a more-or-less normal distribution of letters, as opposed to using 'Content here, content here', making it look like readable English. Many desktop publishing packages and web page editors now use Lorem Ipsum as their default</p></div>
  <div class="tip"><div class="tip-q">Upgrade windows and doors<span>+</span></div></div>
  <div class="tip"><div class="tip-q">Add a pool and outdoor amenities<span>+</span></div></div>
  <div class="tip"><div class="tip-q">Update your landscaping with modern plants<span>+</span></div></div>
</div>

<p class="abs eyebrow" style="left:207px;top:3547px">Have a Question?</p>
<h2 class="abs heading quote-title">Request a Free Quote</h2>
<p class="abs quote-p">We'd love to hear from you! We are an exteriors company specializing in vinyl siding, Northcrest siding, aluminum soffit/fascia, trough.</p>
<div class="btn btn-line" style="left:207px;top:3722px;width:120px;height:30px">Contact Us</div>

<div class="abs form"></div>
<div class="abs field" style="top:3453px">Enter Your Name</div>
<div class="abs field" style="top:3511px">Phone</div>
<div class="abs field" style="top:3568px">Email</div>
<div class="abs field" style="top:3626px">Choose a Service
  <svg width="10" height="6" viewBox="0 0 10 6" fill="none" stroke="currentColor" stroke-width="1.3"><path d="m1 1 4 4 4-4"/></svg></div>
<div class="abs field field-msg" style="top:3684px">Message ...</div>
<div class="abs field" style="top:3812px;height:38px;background:var(--blue);color:#fff;font-size:13px;font-weight:500">Consult Now!
  <svg width="10" height="8" viewBox="0 0 10 8" fill="none" stroke="currentColor" stroke-width="1.3"><path d="M0 4h9M6 1l3 3-3 3"/></svg></div>

<footer class="abs footer" role="img" aria-label="Dimmed photo of a house behind the footer"></footer>
<div class="abs" style="left:88px;top:4032px;width:87px;height:87px;border-radius:50%;border:4px solid var(--blue)"></div>
<p class="abs f-h" style="left:207px;top:4056px">Bramwell Exteriors</p>
<p class="abs" style="left:207px;top:4098px;font-size:22px;color:var(--blue);display:flex;align-items:center;gap:6px">Call Us:
  <svg width="18" height="18" viewBox="0 0 24 24" fill="none" stroke="currentColor" stroke-width="2"><path d="M22 16.9v3a2 2 0 0 1-2.2 2 19.8 19.8 0 0 1-8.6-3.1 19.5 19.5 0 0 1-6-6A19.8 19.8 0 0 1 2.1 4.2 2 2 0 0 1 4.1 2h3a2 2 0 0 1 2 1.7c.1.9.4 1.8.7 2.7a2 2 0 0 1-.5 2.1L8 9.8a16 16 0 0 0 6 6l1.3-1.3a2 2 0 0 1 2.1-.4c.9.3 1.8.6 2.7.7a2 2 0 0 1 1.7 2z"/></svg>
  <span style="color:#fff">780-555-0148</span></p>
<p class="abs footer-text" style="left:207px;top:4129px">e. info@bramwellbuilders.ca</p>
<p class="abs footer-text" style="left:207px;top:4166px;color:var(--blue)">Location:</p>
<p class="abs footer-text" style="left:207px;top:4186px;line-height:20px">4410 Cedar Ridge Road Westhaven,<br>ML 33120</p>

<p class="abs f-h" style="left:616px;top:4056px">Quick Links</p>
<div class="abs footer-text" style="left:616px;top:4083px;line-height:24px">Home<br>Services<br>Meet The Team<br>Blog<br>Contact Us</div>

<p class="abs f-h" style="left:848px;top:4056px">© 2020 Bramwell Exteriors</p>
<p class="abs footer-text" style="left:848px;top:4084px">All Rights Reserved.</p>
<div class="abs social" style="left:849px;top:4120px"></div>
<div class="abs social" style="left:889px;top:4120px;background:var(--blue)"></div>
<div class="abs social" style="left:931px;top:4120px"></div>
<div class="abs social" style="left:971px;top:4120px"></div>
<svg class="abs" style="left:1098px;top:4060px" width="28" height="32" viewBox="0 0 28 32" fill="none" stroke="var(--blue)" stroke-width="2.5"><path d="M3 30 14 3l11 27-11-8z"/></svg>

</body>
</html>
```